Bramblecrest Postcard

I am a real estate agent with a company called Pellworth and Associates. I would like to do two post cards. A Just Listed and a Just Sold card featuring the condominium /villa community named Bramblecrest. I am attached several photos to be used in the design. It will be an oversized postcard and both sides will be in color.

Industry/Entity Type

Real Estate

```html
<!DOCTYPE html>
<html lang="en">
<head>
<meta charset="utf-8">
<title>Bramblecrest Just Listed Postcard</title>
<link href="https://fonts.googleapis.com/css2?family=Tinos:wght@400;700&display=swap" rel="stylesheet">
<style>
:root{
  --stage:#ecebe8;
  --paper:#ffffff;
  --ink:#111111;
  --night:#050505;
  --steel:#a9b8d6;
  --sky-top:#6aa3dc;
  --sky-low:#dfe9f2;
  --leaf:#5c7a3a;
  --sand:#d9c79a;
  --muted:#9d9d9d;
  --rule:#cfcfcf;
}
*{box-sizing:border-box;margin:0;padding:0}
html,body{width:926px;height:1200px;overflow:hidden;background:var(--stage)}
body{position:relative;font-family:"Tinos","Times New Roman",serif;color:var(--ink)}
.card{position:absolute;left:35px;width:857px;height:545px;background:var(--paper);box-shadow:0 2px 8px rgba(0,0,0,.18)}
.card--front{top:40px}
.card--back{top:615px}
.photo{position:absolute}
.hero{left:15px;top:11px;width:555px;height:379px;background:linear-gradient(180deg,var(--sky-top) 0%,var(--sky-low) 45%,#e8d6b0 62%,var(--leaf) 80%,#b9a88d 100%)}
.address-band{position:absolute;left:15px;top:342px;width:555px;height:45px;background:rgba(60,60,60,.45);color:#fff;font-size:24px;line-height:45px;padding-left:20px}
.ribbon{position:absolute;left:569px;top:11px;width:81px;height:560px}
.ribbon-label{position:absolute;left:569px;top:11px;width:81px;height:500px;display:flex;align-items:center;justify-content:center}
.ribbon-label span{display:block;transform:rotate(90deg);white-space:nowrap;font-size:52px;letter-spacing:2px;line-height:1}
.ribbon-label .just{color:var(--ink);position:absolute;top:150px}
.ribbon-label .listed{color:#fff;position:absolute;top:335px}
.thumb{left:653px;width:191px}
.thumb--gym{top:11px;height:123px;background:linear-gradient(180deg,#dfe6ec,#8e9aa6)}
.thumb--court{top:137px;height:126px;background:linear-gradient(180deg,#8fb8e0 0%,#3e6a2e 45%,#5d9a4a 100%)}
.thumb--lounge{top:269px;height:126px;background:linear-gradient(180deg,#f1ece0,#a0683a)}
.thumb--grounds{top:400px;height:132px;background:linear-gradient(180deg,#6aa3dc,#dfe9f2 55%,#5c7a3a)}
.brand{position:absolute;background:var(--steel);display:flex;align-items:center;gap:8px;padding:0 10px;border:3px solid var(--night)}
.brand-mark{width:12px;height:12px;background:var(--night);flex:none}
.brand-name{font-size:17px;color:var(--night);line-height:1.1}
.brand--front{left:15px;top:411px;width:187px;height:97px}
.brand--back{left:228px;top:178px;width:120px;height:60px;padding:0 6px;gap:5px}
.brand--back .brand-name{font-size:11px}
.brand--back .brand-mark{width:8px;height:8px}
.agent{position:absolute;left:215px;top:430px}
.agent-name{font-size:23px;letter-spacing:.5px;margin-bottom:14px}
.agent-line{font-size:17px;line-height:30px}
.back-panel{position:absolute;left:0;top:0;width:376px;height:545px;background:var(--night);color:#fff}
.entry{left:16px;top:13px;width:352px;height:229px;border:1px solid #fff;background:linear-gradient(180deg,var(--sky-top) 0%,#cfe0ef 40%,#4f7a3c 70%,#a9b58c 100%)}
.listing{position:absolute;left:16px;top:255px;width:205px;font-size:15px;line-height:22px}
.listing-name{font-size:19px;margin-bottom:6px}
.fill-rule{display:inline-block;border-bottom:1px solid #fff;height:14px;vertical-align:baseline}
.listing-rule{display:block;width:200px;margin-top:24px}
.listing-price{margin-top:18px}
.map{left:231px;top:258px;width:129px;height:189px;background:linear-gradient(160deg,#d7e6ef 0%,#e9dcc0 60%,#d7e6ef 100%)}
.placeholder{position:absolute;left:384px;top:11px;width:113px;height:137px;background:var(--muted);color:#fff;font-size:20px;text-align:center;display:flex;align-items:center;justify-content:center;line-height:1.3}
.message{position:absolute;left:508px;top:9px;width:150px;font-size:14px;line-height:19px;color:var(--ink)}
.message p+p{margin-top:12px}
.stamp{position:absolute;left:668px;top:16px;width:169px;height:123px;border:1.5px solid var(--ink)}
</style>
</head>
<body>

<section class="card card--front">
  <div class="photo hero" role="img" aria-label="Two-storey villa townhomes with palm trees and garages"></div>
  <div class="address-band">2450 Sandpiper Shore Dr G202 Coral Bend, FL 33900</div>

  <svg class="ribbon" viewBox="0 0 81 560" aria-hidden="true">
    <rect x="0" y="0" width="81" height="265" fill="var(--steel)"/>
    <polygon points="0,265 81,265 81,525 40.5,505 0,525" fill="var(--night)"/>
  </svg>
  <div class="ribbon-label"><span class="just">JUST</span><span class="listed">LISTED</span></div>

  <div class="photo thumb thumb--gym" role="img" aria-label="Community fitness room"></div>
  <div class="photo thumb thumb--court" role="img" aria-label="Tennis court with tree line"></div>
  <div class="photo thumb thumb--lounge" role="img" aria-label="Clubhouse lounge with sofas"></div>
  <div class="photo thumb thumb--grounds" role="img" aria-label="Palm-lined community grounds"></div>

  <div class="brand brand--front"><span class="brand-mark"></span><span class="brand-name">Pellworth and Associates</span></div>

  <div class="agent">
    <h2 class="agent-name">MAREN HOLT</h2>
    <p class="agent-line">941 555 0142</p>
    <p class="agent-line">marenholt@postmail.com</p>
  </div>
</section>

<section class="card card--back">
  <div class="back-panel">
    <div class="photo entry" role="img" aria-label="Bramblecrest entrance sign among palms"></div>
    <div class="brand brand--back"><span class="brand-mark"></span><span class="brand-name">Pellworth and Associates</span></div>

    <div class="listing">
      <h2 class="listing-name">MAREN HOLT</h2>
      <p>2450 Sandpiper Shore Dr<br>G202 Coral Bend, FL 33900</p>
      <span class="fill-rule listing-rule"></span>
      <p>in the Bramblecrest has been listed</p>
      <p class="listing-price">at $ <span class="fill-rule" style="width:62px"></span> &nbsp;on <span class="fill-rule" style="width:72px"></span></p>
    </div>

    <div class="photo map" role="img" aria-label="Regional coastal map showing the community location"></div>
  </div>

  <div class="placeholder">YOUR<br>IMAGE</div>
  <div class="message">
    <p>Please contact me if you are interested in bying or selling property in the area</p>
    <p>941 555 0142<br>marenholt@postmail.com</p>
  </div>
  <div class="stamp"></div>
</section>

</body>
</html>
```